Start up in business consultancy needs a business card

We need the business card's layout (we have already the logo). Our business is concerned on consultancy services delivered to companies on the matter of sustainability. Business card should be enough essentials and professional style.

Side A with the following info:
logo + a space for the claim (still to identify) + website of the company

Side B with the following info:
Name of business card holder + title of the business card holder + address of the company + space for mobile number, phone number, fax number + e-mail of business card holder + graphic details around.

Target Market(s)

Business of any sector

Industry/Entity Type

Business Service

Contact Information for Business Card

Name of the company:
Pianoverde srl
Società Benefit

Address of the company:
Via Lucerna, 7
21047 - Saronno (VA)

Website:
www.pianoverde.it

Name of the BC' holder:
Luca Ferentino

Title:
Co-fondatore

Email:
luca@pianoverde.it

Mobile:
+39 348 915 2074
Phone:
+39 348 915 2074
Fax:
+39 348 915 2074

Font styles to use
Other font styles liked:
• new gothic

```html
<!DOCTYPE html>
<html lang="it">
<head>
<meta charset="utf-8">
<title>Pianoverde srl – Biglietto da visita</title>
<link rel="stylesheet" href="https://fonts.googleapis.com/css2?family=Montserrat:wght@600;700&family=Questrial&display=swap">
<style>
  :root {
    --navy: #1b5480;
    --mint: #00fbaa;
    --teal: #0acb96;
    --white: #ffffff;
    --ghost: #eef4fb;
    --backdrop: #e9e4da;
  }
  * { margin: 0; padding: 0; box-sizing: border-box; }
  html, body { width: 1200px; height: 1200px; overflow: hidden; }
  body { background: var(--backdrop); position: relative; font-family: "Questrial", sans-serif; }

  .card {
    position: absolute; left: 180px; width: 840px; height: 478px;
    border-radius: 40px; overflow: hidden; background: var(--white);
    box-shadow: 0 6px 18px rgba(0,0,0,.18);
  }
  .card--front { top: 68px; }
  .card--back { top: 610px; }

  /* Front */
  .front__band { position: absolute; left: 0; top: 0; width: 100%; height: 300px; background: var(--navy); }
  .front__stripe { position: absolute; left: 0; top: 300px; width: 100%; height: 16px; background: var(--teal); }
  .front__tab { position: absolute; left: 0; top: 0; }
  .brand { position: absolute; left: 112px; top: 56px; display: flex; align-items: center; gap: 28px; }
  .brand__circle { width: 188px; height: 188px; border: 7px solid var(--white); border-radius: 50%; }
  .brand__name { color: var(--white); font-size: 78px; letter-spacing: 1px; line-height: 1; }
  .web-badge {
    position: absolute; left: 266px; top: 312px; width: 306px; height: 46px;
    color: var(--white); font-family: "Montserrat", sans-serif; font-weight: 700; font-size: 25px;
    display: flex; align-items: center; justify-content: center;
  }
  .web-badge svg, .company-badge svg { position: absolute; inset: 0; }
  .web-badge span, .company-badge span { position: relative; }

  /* Back */
  .back__panel { position: absolute; left: 0; top: 0; width: 316px; height: 100%; background: var(--navy); }
  .back__stripe { position: absolute; left: 316px; top: 0; width: 10px; height: 100%; background: var(--teal); }
  .back__accent { position: absolute; left: 0; top: 0; }
  .back__ghost { position: absolute; left: 456px; top: 58px; width: 360px; height: 360px; border: 10px solid var(--ghost); border-radius: 50%; }
  .company-badge {
    position: absolute; left: 34px; top: 72px; width: 244px; height: 46px;
    color: var(--white); font-family: "Montserrat", sans-serif; font-weight: 700; font-size: 25px;
    display: flex; align-items: center; justify-content: center;
  }
  .holder { position: absolute; left: 0; width: 340px; top: 168px; text-align: center; color: var(--white); }
  .holder__name { font-family: "Montserrat", sans-serif; font-weight: 700; font-size: 30px; letter-spacing: .5px; }
  .holder__title { font-size: 22px; margin-top: 2px; }
  .back__mark { position: absolute; left: 104px; top: 293px; width: 112px; height: 112px; border: 5px solid var(--white); border-radius: 50%; display: flex; align-items: center; justify-content: center; }
  .back__mark span { color: var(--white); font-size: 17px; }

  .contacts { position: absolute; left: 0; top: 0; list-style: none; }
  .contacts li { position: absolute; left: 340px; width: 480px; height: 40px; display: flex; align-items: center; }
  .contacts svg { width: 36px; height: 36px; flex: none; }
  .contacts span { position: absolute; left: 74px; color: var(--navy); font-size: 24px; white-space: nowrap; }
</style>
</head>
<body>

<section class="card card--front" aria-label="Fronte">
  <div class="front__band"></div>
  <div class="front__stripe"></div>
  <svg class="front__tab" width="840" height="478" aria-hidden="true">
    <path d="M168 300 H668 L622 358 Q608 374 588 374 H252 Q232 374 218 358 Z" fill="var(--mint)"/>
  </svg>
  <div class="brand">
    <div class="brand__circle"></div>
    <div class="brand__name">pianoverde</div>
  </div>
  <div class="web-badge">
    <svg width="306" height="46" aria-hidden="true">
      <path d="M16 3 H290 L303 23 L290 43 H16 L3 23 Z" fill="none" stroke="var(--white)" stroke-width="4" stroke-linejoin="round"/>
    </svg>
    <span>www.pianoverde.it</span>
  </div>
</section>

<section class="card card--back" aria-label="Retro">
  <div class="back__ghost"></div>
  <div class="back__panel"></div>
  <div class="back__stripe"></div>
  <svg class="back__accent" width="840" height="478" aria-hidden="true">
    <path d="M326 22 L378 68 Q392 82 392 104 V380 Q392 400 376 414 L326 458 Z" fill="var(--mint)"/>
  </svg>

  <div class="company-badge">
    <svg width="244" height="46" aria-hidden="true">
      <path d="M15 3 H229 L241 23 L229 43 H15 L3 23 Z" fill="none" stroke="var(--white)" stroke-width="4" stroke-linejoin="round"/>
    </svg>
    <span>Pianoverde srl</span>
  </div>
  <div class="holder">
    <div class="holder__name">LUCA FERENTINO</div>
    <div class="holder__title">Co-fondatore</div>
  </div>
  <div class="back__mark"><span>pianoverde</span></div>

  <ul class="contacts">
    <li style="top:106px">
      <svg viewBox="0 0 24 24" aria-label="Indirizzo"><path d="M12 2a6.5 6.5 0 0 0-6.5 6.5C5.5 13 12 22 12 22s6.5-9 6.5-13.5A6.5 6.5 0 0 0 12 2zm0 9a2.5 2.5 0 1 1 0-5 2.5 2.5 0 0 1 0 5z" fill="var(--white)"/></svg>
      <span>Via Lucerna, 7,&nbsp;&nbsp; 21047 - Saronno (VA)</span>
    </li>
    <li style="top:165px">
      <svg viewBox="0 0 24 24" aria-label="Cellulare"><path d="M6.6 2.5l3 3.2-1.9 2.6c1.3 2.8 3.3 4.8 6 6.1l2.6-1.9 3.2 3-1.6 3.4C10.4 18.6 5.4 13.6 3.2 4.1z" fill="var(--white)"/></svg>
      <span>+39 348 915 2074</span>
    </li>
    <li style="top:224px">
      <svg viewBox="0 0 24 24" aria-label="Fax"><path d="M7 3h10v4H7zM4 8h16a1 1 0 0 1 1 1v7h-3v-3H6v3H3V9a1 1 0 0 1 1-1zm3 6h10v7H7zm2 2v1h6v-1zm0 2v1h6v-1z" fill="var(--white)"/></svg>
      <span>+39 348 915 2074</span>
    </li>
    <li style="top:283px">
      <svg viewBox="0 0 24 24" aria-label="Email"><path d="M2 5h20v14H2zm2 2v.5l8 6 8-6V7l-8 6z" fill="var(--white)"/></svg>
      <span>luca@pianoverde.it</span>
    </li>
    <li style="top:342px">
      <svg viewBox="0 0 24 24" aria-label="Sito web"><g fill="none" stroke="var(--white)" stroke-width="1.8"><circle cx="12" cy="12" r="9"/><ellipse cx="12" cy="12" rx="4" ry="9"/><path d="M3 12h18M4.5 7.5h15M4.5 16.5h15"/></g></svg>
      <span>www.pianoverde.it</span>
    </li>
  </ul>
</section>

</body>
</html>
```